Ice Cream Cup Design

We need a packaging design for ice cream cups.
We're a London based company called Villa Rosa Dolci and are producers of fresh Italian Artisan Gelato our website is www.villarosadolci.co.uk

We're looking to invest in a cup filling machine to fill 100ml and 500ml cups of gelato.
The 500ml cup will be the same shape and height as the Nordvik Freeze tub with a matching lid design.
The 100ml cup will be of the same shape and height of the Nordvik Freeze Single Serve cup with a matching lid design and includes a spoon inside.

We're looking for edgy clean designs that give an impression of quality and draw attention to the product if it sat on a product shelf. Inspired by packaging such as Ko, Pemberly and Harrowfield we're keen on a black themed packaging with a striking contrast of simple colour and a simple ice cream or gelato image that shows more than one flavour.
This particular design is not boasting any particular flavour, its a uniform design across our whole range of flavours.

Our company logo may be too fussy for this packaging so we would like to include our company ice cream logo and a way to include our company name but still look edgy for example - just like Pemberly Tea - our ice cream logo big G underneath, then 'VILLA ROSA DOLCI' underneath, and below that 'ARTISAN ITALIAN GELATO'. Or anything that inspires and looks good, will draw attention and looks sexy and indulgent and gives an impression of luxury product.

Please check attached document for cup shape and dimensions.

Reason: Christmas and New Year Holiday period resulted in less time for feedback opportunity and new designs to be posted.

Target Market(s)

Target market between 20-40 years old, consumers of quality desserts all year round.

Industry/Entity Type

It Company

Requirements
Must have
• Our Ice Cream Logo
Our name (doesn't need to necessarily have it in our font, can be in bold lettering)
Nice to have
• Limited writing and fuss.
Ideal to have simple clean designs
Should not have
• Eccentric colours and fun childlike images.

```html
<!DOCTYPE html>
<html lang="en">
<head>
<meta charset="utf-8">
<title>Villa Rosa Dolci – Gelato Cup Label</title>
<link rel="stylesheet" href="https://fonts.googleapis.com/css2?family=Cormorant+Garamond:wght@500&family=Oswald:wght@500&family=Roboto+Slab:wght@500&display=swap">
<style>
  :root {
    --page: #f4f4f2;
    --chocolate: #3a1c10;
    --chocolate-light: #5a2e1a;
    --cream: #ece2c4;
    --cream-light: #f3ecd6;
    --gold: #c79a3a;
    --gold-light: #ecd08a;
    --heading: #5c1414;
    --ink: #3b2a22;
    --pill: #8a4a26;
    --pill-text: #f6e9d6;
  }
  * { margin: 0; padding: 0; box-sizing: border-box; }
  html, body {
    width: 1200px; height: 866px; overflow: hidden;
    background: var(--page);
  }
  .label {
    position: absolute; left: 290px; top: 85px;
    width: 620px; height: 696px;
    box-shadow: 0 6px 18px rgba(0,0,0,.25);
  }
  .label-art { position: absolute; inset: 0; display: block; }
  .brand-name {
    position: absolute; top: 250px; left: 0; width: 100%;
    text-align: center;
    font-family: "Cormorant Garamond", serif;
    font-weight: 500; font-size: 52px; color: var(--ink);
  }
  .tagline {
    position: absolute; top: 330px; left: 0; width: 100%;
    text-align: center;
    font-family: "Cormorant Garamond", serif;
    font-weight: 500; font-size: 21px; color: var(--ink);
  }
  .product-line {
    position: absolute; top: 368px; left: 0; width: 100%;
    text-align: center;
    font-family: "Oswald", sans-serif;
    font-weight: 500; font-size: 38px; letter-spacing: 2px;
    color: var(--heading);
  }
  .name-pill {
    position: absolute; left: 158px; top: 638px;
    width: 300px; height: 48px; border-radius: 24px;
    background: var(--pill);
    display: flex; align-items: center; justify-content: center;
    font-family: "Roboto Slab", serif;
    font-weight: 500; font-size: 25px; color: var(--pill-text);
  }
</style>
</head>
<body>
  <main class="label">
    <svg class="label-art" viewBox="0 0 620 696" width="620" height="696">
      <defs>
        <linearGradient id="chocolate-band" x1="0" y1="0" x2="0" y2="1">
          <stop offset="0" stop-color="var(--chocolate)"/>
          <stop offset=".15" stop-color="var(--chocolate-light)"/>
          <stop offset=".3" stop-color="var(--chocolate)"/>
          <stop offset="1" stop-color="var(--chocolate)"/>
        </linearGradient>
        <linearGradient id="gold-edge" x1="0" y1="0" x2="1" y2="0">
          <stop offset="0" stop-color="var(--gold)"/>
          <stop offset=".5" stop-color="var(--gold-light)"/>
          <stop offset="1" stop-color="var(--gold)"/>
        </linearGradient>
        <radialGradient id="cream-panel" cx=".5" cy=".35" r=".7">
          <stop offset="0" stop-color="var(--cream-light)"/>
          <stop offset="1" stop-color="var(--cream)"/>
        </radialGradient>
        <linearGradient id="gelato-tones" x1="0" y1="0" x2="1" y2="1">
          <stop offset="0" stop-color="#e6b8b4"/>
          <stop offset=".35" stop-color="#f4e6e2"/>
          <stop offset=".55" stop-color="#c9545a"/>
          <stop offset=".75" stop-color="#f2dcd6"/>
          <stop offset="1" stop-color="#d48a88"/>
        </linearGradient>
      </defs>

      <rect class="background-band" width="620" height="696" fill="url(#chocolate-band)"/>

      <rect class="gelato-photo" role="img" aria-label="Photo of scooped strawberry and cherry gelato"
            x="0" y="380" width="620" height="316" fill="url(#gelato-tones)"/>

      <path class="cream-panel-edge"
            d="M0 114 C40 96 80 84 130 92 C170 98 200 110 232 96 C262 82 285 70 310 70
               C335 70 358 82 388 96 C420 110 450 98 490 92 C540 84 580 96 620 114
               L620 570 C560 520 480 470 360 452 C220 432 100 430 0 440 Z"
            fill="url(#gold-edge)"/>
      <path class="cream-panel"
            d="M0 122 C40 104 80 92 130 100 C170 106 200 118 232 104 C262 90 285 78 310 78
               C335 78 358 90 388 104 C420 118 450 106 490 100 C540 92 580 104 620 122
               L620 556 C560 508 480 460 360 443 C220 423 100 421 0 431 Z"
            fill="url(#cream-panel)"/>

      <circle class="brand-mark" cx="310" cy="170" r="34" fill="none" stroke="var(--ink)" stroke-width="2"/>
    </svg>

    <h1 class="brand-name">Villa Rosa Dolci</h1>
    <p class="tagline">The House of Italian Ice Cream</p>
    <h2 class="product-line">ARTISAN ITALIAN GELATO</h2>
    <div class="name-pill">VILLA ROSA DOLCI</div>
  </main>
</body>
</html>
```